Post Card Design Bright Lantern Youth

We need a postcard design that will be mailed to all residents offering free pickups of donated clothing. Our foundation is called Bright Lantern Youth, we are a nonprofit charitable organization that provides meals and medical services to children in need in Honduras. Collecting unwanted second-hand clothing generates revenue that helps fund the mission and programs run by our foundation. We would like to offer our pickup services to everyone who has any unwanted reusable clothing.

```html
<!DOCTYPE html>
<html lang="en">
<head>
<meta charset="utf-8">
<title>Bright Lantern Youth – Clothing Pickup Postcard</title>
<link rel="stylesheet" href="https://fonts.googleapis.com/css2?family=Barlow:wght@400;500;600;700&family=Righteous&display=swap">
<style>
  :root {
    --bg: #e4e2ef;
    --white: #ffffff;
    --blue: #0a87c9;
    --magenta: #c0127f;
    --green: #6db33f;
    --ink: #111111;
    --photo-dark: #2a2a2a;
    --photo-mid: #6b6b6b;
    --line: #333333;
  }
  * { margin: 0; padding: 0; box-sizing: border-box; }
  html, body { width: 1150px; height: 1200px; overflow: hidden; background: var(--bg); }
  .stage { position: relative; width: 1533px; height: 1600px; transform: scale(0.75); transform-origin: 0 0; }
  .postcard { position: absolute; background: var(--white); overflow: hidden; font-family: "Barlow", Arial, sans-serif; }
  .postcard-front { left: 163px; top: 180px; width: 875px; height: 558px; }
  .postcard-back { left: 603px; top: 842px; width: 882px; height: 568px; }
  .card-art { position: absolute; inset: 0; width: 100%; height: 100%; }

  .brand { position: absolute; display: flex; align-items: center; gap: 8px; color: var(--green); font-weight: 600; white-space: nowrap; line-height: 1; }
  .brand-dot { border-radius: 50%; background: var(--green); flex: none; }
  .front-brand { left: 28px; top: 44px; font-size: 20px; }
  .front-brand .brand-dot { width: 13px; height: 13px; }
  .back-brand { left: 34px; top: 150px; font-size: 36px; }
  .back-brand .brand-dot { width: 22px; height: 22px; }

  .offer { position: absolute; left: 34px; top: 226px; width: 340px; color: var(--white); }
  .offer-kicker { font-size: 18px; font-weight: 600; letter-spacing: 0.6px; line-height: 1; }
  .offer-title { font-family: "Righteous", "Arial Black", sans-serif; color: var(--magenta); font-size: 62px; line-height: 1; margin-top: 4px; letter-spacing: 1px; }
  .offer-body { margin-top: 18px; font-size: 14px; line-height: 18.8px; text-transform: uppercase; letter-spacing: 0.2px; }
  .pickup-pill { position: absolute; left: 34px; top: 483px; width: 257px; height: 26px; border-radius: 13px; background: var(--white); color: var(--blue); font-weight: 700; font-size: 22px; line-height: 26px; padding-left: 17px; }

  .contact-bar { position: absolute; left: 58px; top: 500px; color: var(--white); font-size: 15px; letter-spacing: 0.3px; line-height: 22px; white-space: nowrap; }
  .contact-row { display: flex; align-items: center; gap: 20px; }
  .contact-icon { width: 14px; height: 14px; flex: none; }
</style>
</head>
<body>
<div class="stage">

  <section class="postcard postcard-front" aria-label="Postcard front">
    <svg class="card-art" viewBox="0 0 875 558" preserveAspectRatio="none">
      <defs>
        <linearGradient id="frontPhotoTone" x1="0" y1="0" x2="1" y2="1">
          <stop offset="0" stop-color="#8a8a8a"/>
          <stop offset="0.5" stop-color="var(--photo-mid)"/>
          <stop offset="1" stop-color="var(--photo-dark)"/>
        </linearGradient>
      </defs>
      <polygon class="panel-blue" points="0,205 215,82 497,480 367,558 0,558" fill="var(--blue)"/>
      <polygon class="panel-green" points="367,558 497,480 552,558" fill="var(--green)"/>
      <polygon class="photo-area" role="img" aria-label="Black and white portrait photo of a young child" points="350,0 875,0 875,558 552,558" fill="url(#frontPhotoTone)"/>
      <polygon class="band-magenta" points="350,0 875,0 875,55 375,110" fill="var(--magenta)" opacity="0.75"/>
      <polygon class="band-magenta" points="495,480 875,265 875,430 545,558 520,558" fill="var(--magenta)" opacity="0.7"/>
    </svg>

    <div class="brand front-brand"><span class="brand-dot"></span>Bright Lantern Youth</div>

    <div class="offer">
      <p class="offer-kicker">GIVE YOUR CLOTHES</p>
      <h1 class="offer-title">NEW LIFE</h1>
      <p class="offer-body">Our nonprofit charity organization, Bright Lantern Youth, is dedicated to helping underprivileged children in Honduras by offering them medical care and meals. The money made from the collection of unwanted used clothing goes toward supporting our foundation's operations and objectives.</p>
    </div>
    <div class="pickup-pill">we'll pick up for free</div>
  </section>

  <section class="postcard postcard-back" aria-label="Postcard back">
    <svg class="card-art" viewBox="0 0 882 568" preserveAspectRatio="none">
      <defs>
        <linearGradient id="backPhotoTone" x1="0" y1="0" x2="1" y2="1">
          <stop offset="0" stop-color="#3a3a3a"/>
          <stop offset="0.55" stop-color="var(--photo-mid)"/>
          <stop offset="1" stop-color="var(--photo-dark)"/>
        </linearGradient>
        <linearGradient id="decorTone" x1="0" y1="0" x2="1" y2="1">
          <stop offset="0" stop-color="#fde8f1"/>
          <stop offset="1" stop-color="#ffffff"/>
        </linearGradient>
      </defs>
      <polygon class="decor-area" role="img" aria-label="Decorative illustrations of hearts, hands, leaves and clothing" points="660,0 882,0 882,568 320,568" fill="url(#decorTone)"/>
      <polygon class="photo-area" role="img" aria-label="Black and white portrait photo of a young child" points="0,0 660,0 320,568 0,568" fill="url(#backPhotoTone)"/>
      <polygon class="band-magenta" points="265,0 660,0 628,55 340,110" fill="var(--magenta)" opacity="0.75"/>
      <polygon class="band-magenta" points="0,275 200,390 440,390 375,475 140,475 0,430" fill="var(--magenta)" opacity="0.7"/>
      <polygon class="contact-band" points="0,492 366,492 320,568 0,568" fill="var(--ink)"/>
      <rect class="stamp-box" x="700" y="110" width="110" height="165" fill="none" stroke="var(--ink)" stroke-width="2.5"/>
      <g class="address-lines" stroke="var(--line)" stroke-width="1.2">
        <line x1="547" y1="315" x2="837" y2="315"/>
        <line x1="527" y1="355" x2="837" y2="355"/>
        <line x1="507" y1="395" x2="837" y2="395"/>
        <line x1="487" y1="435" x2="837" y2="435"/>
        <line x1="470" y1="475" x2="837" y2="475"/>
        <line x1="452" y1="515" x2="837" y2="515"/>
      </g>
    </svg>

    <div class="brand back-brand"><span class="brand-dot"></span>Bright Lantern Youth</div>

    <div class="contact-bar">
      <p class="contact-row">
        <svg class="contact-icon" viewBox="0 0 24 24"><path fill="var(--green)" d="M6.6 10.8a15.1 15.1 0 0 0 6.6 6.6l2.2-2.2c.3-.3.7-.4 1-.2 1.1.4 2.3.6 3.6.6.6 0 1 .4 1 1V20c0 .6-.4 1-1 1A17 17 0 0 1 3 4c0-.6.4-1 1-1h3.5c.6 0 1 .4 1 1 0 1.3.2 2.5.6 3.6.1.3 0 .7-.2 1z"/></svg>
        (555) 014-2290
      </p>
      <p class="contact-row">
        <svg class="contact-icon" viewBox="0 0 24 24"><rect x="2" y="5" width="20" height="14" fill="none" stroke="var(--green)" stroke-width="2.4"/><path d="M2 5l10 8 10-8" fill="none" stroke="var(--green)" stroke-width="2.4"/></svg>
        INFO@BRIGHTLANTERN.ORG
      </p>
    </div>
  </section>

</div>
</body>
</html>
```